Business Card Design Project

Attached is a rough business card design. We like this general design but we feel that the layout, text, color can use improvement and we seek the help of a professional designer.
We have a television and film production company based in New York. We need our cards for television network executives, other production executives, financiers etc. We deal with creative types as well as business people so we need the card to be interesting and edgy just like the name of our company - KICKTHEDOOR. The design should reflect the edgy, punk rock attitude of our company.
We prefer orange typeface for the logo but we're open to other ideas. I am attaching our existing business card and other files to help with the design.
Thank you in advance!!
Updates
Target Market(s)
Television and film producers, television network executives, other production executives, financiers, distribution companies
Industry/Entity Type
Film Production
Requirements
Must have
- I am attaching a photo of the company mascot which is a dog. We prefer to have the dog's photo as part of the card but we're open to the other ideas.
Name, phone number, email

```html
<!DOCTYPE html>
<html lang="en">
<head>
<meta charset="utf-8">
<title>KICKTHEDOOR – Business Card</title>
<link href="https://fonts.googleapis.com/css2?family=Open+Sans:wght@400;600&family=Pinyon+Script&display=swap" rel="stylesheet">
<style>
  :root {
    --backdrop: #e9e6e2;
    --card: #000000;
    --brand-orange: #e8772a;
    --text-light: #ffffff;
    --photo-light: #d9a68e;
    --photo-mid: #8f5f4e;
  }
  * { margin: 0; padding: 0; box-sizing: border-box; }
  html, body {
    width: 1200px; height: 1149px; overflow: hidden;
    background: var(--backdrop);
  }
  .canvas { position: relative; width: 1200px; height: 1149px; }
  .card {
    position: absolute; left: 299px; top: 95px;
    width: 567px; height: 990px;
    background: var(--card);
    border-radius: 30px;
    overflow: hidden;
    font-family: "Open Sans", Arial, sans-serif;
    color: var(--text-light);
  }
  .mascot-photo {
    position: absolute; left: 0; top: 0;
    width: 567px; height: 990px;
    background: radial-gradient(circle 340px at 500px 640px,
      var(--photo-light) 0%,
      var(--photo-mid) 45%,
      rgba(0, 0, 0, 0) 100%);
  }
  .brand-name {
    position: absolute; top: 52px; left: 0; width: 100%;
    text-align: center;
    font-weight: 600;
    font-size: 50px;
    letter-spacing: 2px;
    color: var(--brand-orange);
  }
  .person { position: absolute; top: 168px; left: 0; width: 578px; text-align: center; }
  .person-name {
    font-family: "Pinyon Script", cursive;
    font-size: 48px; line-height: 1.1;
  }
  .person-title { font-size: 24px; line-height: 1.2; }
  .contact { position: absolute; left: 40px; top: 828px; list-style: none; }
  .contact li {
    display: flex; align-items: center;
    height: 41px; font-size: 23px;
  }
  .contact svg { width: 24px; height: 24px; margin-right: 22px; flex: none; }
</style>
</head>
<body>
<div class="canvas">
  <div class="card">
    <div class="mascot-photo" role="img" aria-label="Photo of the company mascot, a fawn French bulldog lying down with a small toy ball"></div>

    <div class="brand-name">kickthedoor</div>

    <div class="person">
      <div class="person-name">Daniel Moreno</div>
      <div class="person-title">Director</div>
    </div>

    <ul class="contact">
      <li>
        <svg viewBox="0 0 24 24"><path d="M6.6 2.5 9.5 6.5 7.6 8.6c1 2.7 3.1 5.1 5.8 6.5l2-2 4 2.8-1.6 3.6c-.4.9-1.4 1.3-2.3 1C9 18.6 4.4 13.6 3 7c-.2-.9.3-1.8 1.1-2.2Z" fill="var(--brand-orange)"/></svg>
        (917) 555-0186
      </li>
      <li>
        <svg viewBox="0 0 24 24"><circle cx="12" cy="12" r="4" fill="none" stroke="var(--brand-orange)" stroke-width="2.6"/><path d="M16 8v5.5c0 2 2.8 2.4 3.6.4C21.5 8 17.5 2.8 12 2.8a9.2 9.2 0 1 0 5 17" fill="none" stroke="var(--brand-orange)" stroke-width="2.6" stroke-linecap="round"/></svg>
        daniel@kickthedoor.com
      </li>
      <li>
        <svg viewBox="0 0 24 24" fill="none" stroke="var(--brand-orange)" stroke-width="1.8"><circle cx="12" cy="12" r="10"/><ellipse cx="12" cy="12" rx="4.5" ry="10"/><path d="M2 12h20M4 6.5h16M4 17.5h16"/></svg>
        www.kickthedoor.com
      </li>
    </ul>
  </div>
</div>
</body>
</html>
```